WordPress e-commerce new website design

Note: Completely changed the whole website design. Do not use red colors for the design.

We are seeking a talented website designer to create a WordPress e-commerce website for our business. The website will primarily focus on pre-purchase inspections for vehicles, with additional pages for parts, trucks/trailers, finance, and general information.

**Pages:**
1. Home
2. About
3. Pre-purchase Inspections
4. Parts
5. Trucks/Trailers
6. Finance

**Key Features:**
- Home page featuring a spot for a feature video
- Parts and trucks/trailers pages with multiple photos and videos for each item
- Pre-purchase inspections page with showcase video banners and sliders
- Cart functionality for parts
- Simple payment gateways for pre-purchase inspections, including Basic, Premium, and Extreme inspection levels, with corresponding prices
- Option for Fleet Inspection (3 or more vehicles) with a special quote request button
- Pop-up window on the home page prompting users to visit the pre-purchase inspections page
- Yellow payment buttons for easy visibility and user interaction

**Color Scheme:**
The designer can choose colors from blue, gold, yellow, black, white, and light gray.

**Requirements:**
- Proficiency in WordPress and e-commerce website design
- Experience with implementing payment gateways and cart functionality
- Ability to create visually appealing designs that align with our brand identity
- Strong attention to detail for creating new Design for semi-truck pre-purchase inspections website

```html
<!DOCTYPE html>
<html lang="en">
<head>
<meta charset="utf-8">
<title>Torvane – Home</title>
<link href="https://fonts.googleapis.com/css2?family=Orbitron:wght@700;900&family=Roboto:wght@400;500&family=Roboto+Condensed:wght@400;700&display=swap" rel="stylesheet">
<style>
:root{
  --board:#eceef2;
  --accent:#0b3d91;
  --accent-dark:#082a66;
  --gold:#c9a227;
  --ink:#111;
  --white:#fff;
  --band:#f1f3f6;
  --popup:#ffffff;
  --yellow:#f2d600;
  --muted:#444;
}
*{margin:0;padding:0;box-sizing:border-box}
html,body{width:813px;height:1200px;overflow:hidden;background:var(--board)}
body{position:relative;font-family:"Roboto",sans-serif;color:var(--ink)}
.panel{position:absolute;top:23px;width:367px;height:1155px;background:var(--white);overflow:hidden}
.panel--home{left:26px}
.panel--popup{left:420px}
.abs{position:absolute}
.fill-accent{fill:var(--accent)}
.fill-gold{fill:var(--gold)}
.fill-ink{fill:#000}
.btn{position:absolute;display:flex;align-items:center;justify-content:center;border-radius:8px;font-family:"Roboto Condensed",sans-serif;font-weight:700;font-size:5px;color:var(--white);background:var(--accent);white-space:nowrap}
.btn--yellow{background:var(--yellow);color:var(--ink)}
.btn--white{background:var(--white);color:var(--ink)}
.heading{font-family:"Orbitron",sans-serif;font-weight:900;font-size:13px;letter-spacing:.5px;white-space:nowrap}
.heading .accent{color:var(--accent)}
.chev{position:absolute;width:14px;height:6px}

.brand{left:34px;top:8px;font-family:"Roboto Condensed",sans-serif;font-weight:700;font-size:15px;letter-spacing:1px;color:var(--ink)}
.contact-chip{display:flex;align-items:center;gap:2px;top:4px;font-size:4.2px;line-height:5px;white-space:nowrap}
.contact-chip b{color:var(--accent);font-weight:500}
.ico{width:11px;height:11px;border-radius:50%;background:var(--accent);display:flex;align-items:center;justify-content:center;border:1px solid #c9d3e6;flex:none}
.nav{top:20px;left:146px;font-size:4.5px}
.nav span{position:absolute;white-space:nowrap}
.nav .active{color:var(--accent)}

.hero-photo{left:0;top:29px;width:367px;height:220px}
.hero-welcome{top:66px;width:367px;text-align:center;font-family:"Roboto Condensed",sans-serif;font-size:11px;color:var(--ink)}
.hero-brand{top:78px;width:367px;text-align:center;font-family:"Orbitron",sans-serif;font-weight:900;font-size:24px;color:var(--accent);letter-spacing:1px}

.about-frame{left:34px;top:276px;width:136px;height:145px;border:1px solid var(--accent);border-radius:5px;padding:3px 0}
.about-photo{width:100%;height:100%;border-radius:3px;background:linear-gradient(135deg,#3a3a3e,#1e3566 35%,#2b2d35 60%,#8f8f92)}
.about-title{left:183px;top:286px}
.copy{font-size:4.6px;line-height:8.6px;color:var(--muted)}
.about-copy{left:183px;top:324px;width:150px}

.parts-band{left:0;top:451px;width:367px;height:232px;background:var(--band)}
.section-title{width:367px;text-align:center}
.part-card{border:1px solid var(--accent);border-radius:5px;background:var(--band);text-align:center}
.part-card--feature{background:linear-gradient(180deg,#23262e,#4a3d1c 55%,#15161a);border:1px solid #222;border-radius:5px;color:var(--white);text-align:center;box-shadow:0 2px 4px rgba(0,0,0,.3)}
.part-img{position:absolute;border-radius:3px}
.part-name{position:absolute;width:100%;font-family:"Orbitron",sans-serif;font-weight:900;font-size:6.5px;color:var(--accent)}
.part-card--feature .part-name{color:var(--white);font-size:8px}
.part-text{position:absolute;width:100%;font-size:4.5px;color:#333;white-space:nowrap}
.part-card--feature .part-text{font-size:5.5px;color:#eee}
.part-price{position:absolute;width:100%;font-family:"Orbitron",sans-serif;font-weight:900;font-size:10px;color:var(--ink)}
.part-card--feature .part-price{font-size:12px;color:var(--white)}
.dot{position:absolute;width:4px;height:4px;border-radius:50%;background:var(--ink);top:659px}
.dot--active{background:var(--accent);box-shadow:0 0 0 1px var(--white),0 0 0 1.6px var(--accent)}

.price-card{position:absolute;top:750px;width:96px;height:97px;border-radius:5px;background:linear-gradient(160deg,#2a2a2a,#141414 60%,#222);color:var(--white);text-align:center}
.price-name{position:absolute;top:13px;width:100%;font-family:"Orbitron",sans-serif;font-weight:900;font-size:10px;letter-spacing:.3px}
.price-text{position:absolute;top:28px;left:5px;right:5px;font-size:4.5px;line-height:8.6px;color:#ddd}
.price-amount{position:absolute;top:56px;width:100%;font-family:"Orbitron",sans-serif;font-weight:900;font-size:9px}

.fleet{left:0;top:877px;width:367px;height:107px;background:var(--accent);color:var(--white);text-align:center}
.fleet-title{position:absolute;top:12px;width:100%;font-family:"Orbitron",sans-serif;font-weight:900;font-size:13px;letter-spacing:.5px}
.fleet-copy{position:absolute;top:35px;left:44px;width:269px;font-size:4.6px;line-height:8.6px}

.footer-shape{left:0;top:980px;width:367px;height:175px}
.footer-brand{left:34px;top:1062px;font-family:"Roboto Condensed",sans-serif;font-weight:700;font-size:13px;letter-spacing:1px;color:var(--white)}
.footer-head{font-family:"Roboto Condensed",sans-serif;font-size:6px;color:var(--white)}
.footer-link{font-size:5px;color:var(--white)}
.footer-row{display:flex;align-items:center;gap:5px;font-size:5px;color:var(--white);white-space:nowrap}
.social{width:14px;height:14px;border-radius:50%;border:1px solid var(--white);top:1065px}
.copyright{top:1138px;left:0;width:367px;text-align:center;font-size:4.5px;color:var(--white)}

.shade{left:0;top:0;width:367px;height:1155px;background:rgba(0,0,0,.56)}
.popup{left:69px;top:46px;width:230px;height:135px;background:var(--popup);border-radius:5px;text-align:center}
.popup-title{position:absolute;top:27px;width:100%;font-family:"Orbitron",sans-serif;font-weight:900;font-size:9.5px;line-height:13px;letter-spacing:.4px}
.popup-copy{position:absolute;top:55px;left:20px;right:20px;font-size:6px;line-height:9.5px;color:#222}
</style>
</head>
<body>

<section class="panel panel--home">
  <div class="abs brand">TORVANE</div>
  <div class="abs contact-chip" style="left:133px"><span class="ico"><svg width="6" height="5" viewBox="0 0 10 8"><rect x=".5" y=".5" width="9" height="7" fill="none" stroke="#fff"/><path d="M.5.5L5 4 9.5.5" fill="none" stroke="#fff"/></svg></span><span><b>Mail:</b><br>info@torvane.com</span></div>
  <div class="abs contact-chip" style="left:201px"><span class="ico"><svg width="6" height="6" viewBox="0 0 10 10"><path d="M2 1l2 2-1 1.5c.8 1.5 1.8 2.5 3.3 3.3L7.8 6.8l2 2-1.3 1.2C4.6 9.6.4 5.4 0 1.5z" fill="#fff"/></svg></span><span><b>Phone No:</b><br>+1(555)014 2290</span></div>
  <div class="btn" style="left:264px;top:4px;width:39px;height:12px">Contact Us</div>
  <svg class="abs" style="left:313px;top:6px" width="9" height="8" viewBox="0 0 9 8"><path d="M0 1h1.6l1 4h4.6l1-3H2.4" fill="none" stroke="#0b3d91" stroke-width="1"/><circle cx="3.2" cy="7" r=".8" class="fill-accent"/><circle cx="6.4" cy="7" r=".8" class="fill-accent"/></svg>
  <svg class="abs" style="left:325px;top:6px" width="9" height="8" viewBox="0 0 10 9"><path class="fill-accent" d="M5 9L1 5C-.5 3.5.5 0 3 .5 4 .7 4.6 1.5 5 2c.4-.5 1-1.3 2-1.5C9.5 0 10.5 3.5 9 5z"/></svg>
  <div class="abs nav">
    <span class="active" style="left:0">Home</span><span style="left:21px">About</span><span style="left:44px">Pre-purchase Inspections</span><span style="left:108px">Parts</span><span style="left:128px">Trucks/Trailers</span><span style="left:170px">Finance</span>
  </div>

  <svg class="abs hero-photo" viewBox="0 29 367 220" role="img" aria-label="Row of colourful semi-trucks parked under a cloudy mountain sky">
    <defs>
      <linearGradient id="heroSky1" x1="0" y1="0" x2="0" y2="1"><stop offset="0" stop-color="#dfe5ee"/><stop offset=".35" stop-color="#9aa6b8"/><stop offset=".55" stop-color="#d9b53a"/><stop offset=".75" stop-color="#2f4a86"/><stop offset="1" stop-color="#2b2b30"/></linearGradient>
    </defs>
    <path d="M0 29H367V200Q250 206 183 245Q116 206 0 200Z" fill="url(#heroSky1)"/>
    <path class="fill-accent" d="M0 198Q118 204 183 246Q248 204 367 198V204Q250 212 183 249Q116 212 0 204Z"/>
  </svg>
  <div class="abs hero-welcome">Welcome To</div>
  <div class="abs hero-brand">TORVANE</div>
  <div class="btn" style="left:163px;top:104px;width:39px;height:12px">Get Started</div>

  <div class="abs about-frame"><div class="about-photo" role="img" aria-label="Mechanic in overalls servicing a truck engine"></div></div>
  <div class="abs heading about-title">ABOUT <span class="accent">US</span></div>
  <svg class="chev" style="left:184px;top:303px" viewBox="0 0 14 6"><path class="fill-accent" d="M0 0L7 6 14 0 7 3z"/></svg>
  <p class="abs copy about-copy">Lorem ipsum dolor sit amet, consectetur adipiscing elit, sed do iusmod tempor incididunt ut labore et dolore magna aliqua. Quis endisse trices gravida. Risus commodo viverra maecenas accumsan lacus isis.Lorem ipsum dolor sit amet, consectetur adipiscing elit, sed do eiusmod mpor incididunt ut labore et dolore magna aliqua. Quis ipsum rices gravidafr. Risus commodo viverra maecenas accumsan lacus vel facilisis. Lorem ipsum dolor sit amet, consectetur adipiscing elit, sed do eiusmod mpor incididunt ut labore et dolore magna aliqua.</p>
  <div class="btn" style="left:183px;top:397px;width:40px;height:12px">Read More</div>

  <div class="abs parts-band"></div>
  <div class="abs heading section-title" style="top:468px">OUR <span class="accent">PARTS</span></div>
  <svg class="chev" style="left:176px;top:486px" viewBox="0 0 14 6"><path class="fill-accent" d="M0 0L7 6 14 0 7 3z"/></svg>

  <div class="abs part-card" style="left:51px;top:519px;width:84px;height:117px">
    <div class="part-img" role="img" aria-label="Truck engine block" style="left:14px;top:9px;width:56px;height:51px;background:radial-gradient(circle,#9a9a9a,#5a5550 60%,transparent 72%)"></div>
    <div class="part-name" style="top:64px">ENGINE</div>
    <div class="part-text" style="top:74px">Lorem ipsum dolor sit amet,</div>
    <div class="part-price" style="top:81px">$577</div>
    <div class="btn" style="left:21px;top:95px;width:40px;height:11px">Buy Now</div>
  </div>
  <div class="abs part-card" style="left:233px;top:519px;width:80px;height:117px">
    <div class="part-img" role="img" aria-label="Truck tyre" style="left:14px;top:9px;width:46px;height:51px;background:radial-gradient(circle,#bbb 18%,#222 22%,#333 60%,transparent 68%)"></div>
    <div class="part-name" style="top:64px">TYRE</div>
    <div class="part-text" style="top:74px">Lorem ipsum dolor sit amet,</div>
    <div class="part-price" style="top:81px">$177</div>
    <div class="btn" style="left:20px;top:95px;width:40px;height:11px">Buy Now</div>
  </div>
  <div class="abs part-card--feature" style="left:133px;top:507px;width:100px;height:141px">
    <div class="part-img" role="img" aria-label="Truck cab front" style="left:24px;top:10px;width:52px;height:54px;background:linear-gradient(160deg,#2f63c4,#0b3d91 70%,#333)"></div>
    <div class="part-name" style="top:69px">BUMPPER</div>
    <div class="part-text" style="top:79px">Lorem ipsum dolor sit amet,</div>
    <div class="part-price" style="top:88px">$377</div>
    <div class="btn" style="left:26px;top:105px;width:48px;height:13px;font-size:6px">Buy Now</div>
  </div>
  <span class="dot" style="left:173px"></span><span class="dot dot--active" style="left:181px"></span><span class="dot" style="left:189px"></span>

  <div class="abs heading section-title" style="top:712px">OUR <span class="accent">PRISING</span></div>
  <svg class="chev" style="left:176px;top:730px" viewBox="0 0 14 6"><path class="fill-accent" d="M0 0L7 6 14 0 7 3z"/></svg>
  <div class="price-card" style="left:34px" role="img" aria-label="Basic inspection plan on workshop backdrop">
    <div class="price-name">BASIC</div>
    <div class="price-text">Lorem ipsum dolor sit amet, onsectetur adipiscing elit, sed do eiusmod tempor aliqua.</div>
    <div class="price-amount">$400</div>
    <div class="btn btn--yellow" style="left:28px;top:69px;width:40px;height:12px">Buy Now</div>
  </div>
  <div class="price-card" style="left:136px" role="img" aria-label="Premium inspection plan on workshop backdrop">
    <div class="price-name">PREMIUM</div>
    <div class="price-text">Lorem ipsum dolor sit amet, onsectetur adipiscing elit, sed do eiusmod tempor aliqua.</div>
    <div class="price-amount">320</div>
    <div class="btn btn--yellow" style="left:28px;top:69px;width:40px;height:12px">Buy Now</div>
  </div>
  <div class="price-card" style="left:237px" role="img" aria-label="Extreme inspection plan on workshop backdrop">
    <div class="price-name">EXTREME</div>
    <div class="price-text">Lorem ipsum dolor sit amet, onsectetur adipiscing elit, sed do eiusmod tempor aliqua.</div>
    <div class="price-amount">350</div>
    <div class="btn btn--yellow" style="left:28px;top:69px;width:40px;height:12px">Buy Now</div>
  </div>

  <div class="abs fleet">
    <div class="fleet-title">FLEET INSPECTION</div>
    <p class="fleet-copy">Lorem ipsum dolor sit amet, consectetur adipiscing elit, sed do eiusmod tempor incididunt ut labore et dolore magna aliqua. Quis ipsum suspendisse ultrices gravida. Risus commodo viverra maecenas accumsan lacus vel facilisis.Lorem ipsum dolor sit amet, consectetur adipiscing elit, sed do eiusmod tempor incididunt ut labore et dolore magna aliqua. Quis ipsum suspendisse ultrices gravida. Risus commodo viverra maecenas accumsan lacus vel facilisis.</p>
    <div class="btn btn--white" style="left:164px;top:74px;width:40px;height:12px">Get A Quote</div>
  </div>

  <svg class="abs footer-shape" viewBox="0 980 367 175">
    <path class="fill-accent" d="M0 1032Q116 1024 183 982Q250 1024 367 1032V1155H0Z"/>
    <path class="fill-ink" d="M0 1037Q116 1030 183 988Q250 1030 367 1037V1155H0Z"/>
  </svg>
  <div class="abs footer-brand">TORVANE</div>
  <div class="abs footer-head" style="left:122px;top:1050px">Quick Links</div>
  <div class="abs footer-link" style="left:122px;top:1065px">Home</div>
  <div class="abs footer-link" style="left:122px;top:1075px">About</div>
  <div class="abs footer-link" style="left:122px;top:1085px">Pre-purchase Inspections</div>
  <div class="abs footer-link" style="left:122px;top:1095px">Parts</div>
  <div class="abs footer-link" style="left:122px;top:1105px">Trucks/Trailers</div>
  <div class="abs footer-link" style="left:122px;top:1115px">Finance</div>
  <div class="abs footer-head" style="left:192px;top:1051px">Contact Us</div>
  <div class="abs footer-row" style="left:192px;top:1068px"><span class="ico"><svg width="6" height="5" viewBox="0 0 10 8"><rect x=".5" y=".5" width="9" height="7" fill="none" stroke="#fff"/><path d="M.5.5L5 4 9.5.5" fill="none" stroke="#fff"/></svg></span>info@torvane.com</div>
  <div class="abs footer-row" style="left:192px;top:1088px"><span class="ico"><svg width="5" height="7" viewBox="0 0 6 8"><path d="M3 8S0 4.5 0 3a3 3 0 016 0c0 1.5-3 5-3 5z" fill="#fff"/><circle cx="3" cy="3" r="1" class="fill-accent"/></svg></span>Lorem ipsum,torvane,USA</div>
  <div class="abs footer-row" style="left:192px;top:1107px"><span class="ico"><svg width="6" height="6" viewBox="0 0 10 10"><path d="M2 1l2 2-1 1.5c.8 1.5 1.8 2.5 3.3 3.3L7.8 6.8l2 2-1.3 1.2C4.6 9.6.4 5.4 0 1.5z" fill="#fff"/></svg></span>+1(555)014 2290</div>
  <div class="abs footer-head" style="left:283px;top:1051px">Follow Us</div>
  <span class="abs social" style="left:283px"></span><span class="abs social" style="left:301px"></span><span class="abs social" style="left:318px"></span>
  <div class="abs copyright">Copyright © 2024 Torvane. | All Rights Reserved</div>
</section>

<section class="panel panel--popup">
  <div class="abs brand">TORVANE</div>
  <div class="abs contact-chip" style="left:133px"><span class="ico"><svg width="6" height="5" viewBox="0 0 10 8"><rect x=".5" y=".5" width="9" height="7" fill="none" stroke="#fff"/><path d="M.5.5L5 4 9.5.5" fill="none" stroke="#fff"/></svg></span><span><b>Mail:</b><br>info@torvane.com</span></div>
  <div class="abs contact-chip" style="left:201px"><span class="ico"><svg width="6" height="6" viewBox="0 0 10 10"><path d="M2 1l2 2-1 1.5c.8 1.5 1.8 2.5 3.3 3.3L7.8 6.8l2 2-1.3 1.2C4.6 9.6.4 5.4 0 1.5z" fill="#fff"/></svg></span><span><b>Phone No:</b><br>+1(555)014 2290</span></div>
  <div class="btn" style="left:264px;top:4px;width:39px;height:12px">Contact Us</div>
  <svg class="abs" style="left:313px;top:6px" width="9" height="8" viewBox="0 0 9 8"><path d="M0 1h1.6l1 4h4.6l1-3H2.4" fill="none" stroke="#0b3d91" stroke-width="1"/><circle cx="3.2" cy="7" r=".8" class="fill-accent"/><circle cx="6.4" cy="7" r=".8" class="fill-accent"/></svg>
  <svg class="abs" style="left:325px;top:6px" width="9" height="8" viewBox="0 0 10 9"><path class="fill-accent" d="M5 9L1 5C-.5 3.5.5 0 3 .5 4 .7 4.6 1.5 5 2c.4-.5 1-1.3 2-1.5C9.5 0 10.5 3.5 9 5z"/></svg>
  <div class="abs nav">
    <span class="active" style="left:0">Home</span><span style="left:21px">About</span><span style="left:44px">Pre-purchase Inspections</span><span style="left:108px">Parts</span><span style="left:128px">Trucks/Trailers</span><span style="left:170px">Finance</span>
  </div>

  <svg class="abs hero-photo" viewBox="0 29 367 220" role="img" aria-label="Row of colourful semi-trucks parked under a cloudy mountain sky">
    <defs>
      <linearGradient id="heroSky2" x1="0" y1="0" x2="0" y2="1"><stop offset="0" stop-color="#dfe5ee"/><stop offset=".35" stop-color="#9aa6b8"/><stop offset=".55" stop-color="#d9b53a"/><stop offset=".75" stop-color="#2f4a86"/><stop offset="1" stop-color="#2b2b30"/></linearGradient>
    </defs>
    <path d="M0 29H367V200Q250 206 183 245Q116 206 0 200Z" fill="url(#heroSky2)"/>
    <path class="fill-accent" d="M0 198Q118 204 183 246Q248 204 367 198V204Q250 212 183 249Q116 212 0 204Z"/>
  </svg>

  <div class="abs about-frame"><div class="about-photo" role="img" aria-label="Mechanic in overalls servicing a truck engine"></div></div>
  <div class="abs heading about-title">ABOUT <span class="accent">US</span></div>
  <svg class="chev" style="left:184px;top:303px" viewBox="0 0 14 6"><path class="fill-accent" d="M0 0L7 6 14 0 7 3z"/></svg>
  <p class="abs copy about-copy">Lorem ipsum dolor sit amet, consectetur adipiscing elit, sed do iusmod tempor incididunt ut labore et dolore magna aliqua. Quis endisse trices gravida. Risus commodo viverra maecenas accumsan lacus isis.Lorem ipsum dolor sit amet, consectetur adipiscing elit, sed do eiusmod mpor incididunt ut labore et dolore magna aliqua. Quis ipsum rices gravidafr. Risus commodo viverra maecenas accumsan lacus vel facilisis. Lorem ipsum dolor sit amet, consectetur adipiscing elit, sed do eiusmod mpor incididunt ut labore et dolore magna aliqua.</p>
  <div class="btn" style="left:183px;top:397px;width:40px;height:12px">Read More</div>

  <div class="abs parts-band"></div>
  <div class="abs heading section-title" style="top:468px">OUR <span class="accent">PARTS</span></div>
  <svg class="chev" style="left:176px;top:486px" viewBox="0 0 14 6"><path class="fill-accent" d="M0 0L7 6 14 0 7 3z"/></svg>
  <div class="abs part-card" style="left:51px;top:519px;width:84px;height:117px">
    <div class="part-img" role="img" aria-label="Truck engine block" style="left:14px;top:9px;width:56px;height:51px;background:radial-gradient(circle,#9a9a9a,#5a5550 60%,transparent 72%)"></div>
    <div class="part-name" style="top:64px">ENGINE</div>
    <div class="part-text" style="top:74px">Lorem ipsum dolor sit amet,</div>
    <div class="part-price" style="top:81px">$577</div>
    <div class="btn" style="left:21px;top:95px;width:40px;height:11px">Buy Now</div>
  </div>
  <div class="abs part-card" style="left:233px;top:519px;width:80px;height:117px">
    <div class="part-img" role="img" aria-label="Truck tyre" style="left:14px;top:9px;width:46px;height:51px;background:radial-gradient(circle,#bbb 18%,#222 22%,#333 60%,transparent 68%)"></div>
    <div class="part-name" style="top:64px">TYRE</div>
    <div class="part-text" style="top:74px">Lorem ipsum dolor sit amet,</div>
    <div class="part-price" style="top:81px">$177</div>
    <div class="btn" style="left:20px;top:95px;width:40px;height:11px">Buy Now</div>
  </div>
  <div class="abs part-card--feature" style="left:133px;top:507px;width:100px;height:141px">
    <div class="part-img" role="img" aria-label="Truck cab front" style="left:24px;top:10px;width:52px;height:54px;background:linear-gradient(160deg,#2f63c4,#0b3d91 70%,#333)"></div>
    <div class="part-name" style="top:69px">BUMPPER</div>
    <div class="part-text" style="top:79px">Lorem ipsum dolor sit amet,</div>
    <div class="part-price" style="top:88px">$377</div>
    <div class="btn" style="left:26px;top:105px;width:48px;height:13px;font-size:6px">Buy Now</div>
  </div>
  <span class="dot" style="left:173px"></span><span class="dot dot--active" style="left:181px"></span><span class="dot" style="left:189px"></span>

  <div class="abs heading section-title" style="top:712px">OUR <span class="accent">PRISING</span></div>
  <svg class="chev" style="left:176px;top:730px" viewBox="0 0 14 6"><path class="fill-accent" d="M0 0L7 6 14 0 7 3z"/></svg>
  <div class="price-card" style="left:34px" role="img" aria-label="Basic inspection plan on workshop backdrop">
    <div class="price-name">BASIC</div>
    <div class="price-text">Lorem ipsum dolor sit amet, onsectetur adipiscing elit, sed do eiusmod tempor aliqua.</div>
    <div class="price-amount">$400</div>
    <div class="btn btn--yellow" style="left:28px;top:69px;width:40px;height:12px">Buy Now</div>
  </div>
  <div class="price-card" style="left:136px" role="img" aria-label="Premium inspection plan on workshop backdrop">
    <div class="price-name">PREMIUM</div>
    <div class="price-text">Lorem ipsum dolor sit amet, onsectetur adipiscing elit, sed do eiusmod tempor aliqua.</div>
    <div class="price-amount">320</div>
    <div class="btn btn--yellow" style="left:28px;top:69px;width:40px;height:12px">Buy Now</div>
  </div>
  <div class="price-card" style="left:237px" role="img" aria-label="Extreme inspection plan on workshop backdrop">
    <div class="price-name">EXTREME</div>
    <div class="price-text">Lorem ipsum dolor sit amet, onsectetur adipiscing elit, sed do eiusmod tempor aliqua.</div>
    <div class="price-amount">350</div>
    <div class="btn btn--yellow" style="left:28px;top:69px;width:40px;height:12px">Buy Now</div>
  </div>

  <div class="abs fleet">
    <div class="fleet-title">FLEET INSPECTION</div>
    <p class="fleet-copy">Lorem ipsum dolor sit amet, consectetur adipiscing elit, sed do eiusmod tempor incididunt ut labore et dolore magna aliqua. Quis ipsum suspendisse ultrices gravida. Risus commodo viverra maecenas accumsan lacus vel facilisis.Lorem ipsum dolor sit amet, consectetur adipiscing elit, sed do eiusmod tempor incididunt ut labore et dolore magna aliqua. Quis ipsum suspendisse ultrices gravida. Risus commodo viverra maecenas accumsan lacus vel facilisis.</p>
    <div class="btn btn--white" style="left:164px;top:74px;width:40px;height:12px">Get A Quote</div>
  </div>

  <svg class="abs footer-shape" viewBox="0 980 367 175">
    <path class="fill-accent" d="M0 1032Q116 1024 183 982Q250 1024 367 1032V1155H0Z"/>
    <path class="fill-ink" d="M0 1037Q116 1030 183 988Q250 1030 367 1037V1155H0Z"/>
  </svg>
  <div class="abs footer-brand">TORVANE</div>
  <div class="abs footer-head" style="left:122px;top:1050px">Quick Links</div>
  <div class="abs footer-link" style="left:122px;top:1065px">Home</div>
  <div class="abs footer-link" style="left:122px;top:1075px">About</div>
  <div class="abs footer-link" style="left:122px;top:1085px">Pre-purchase Inspections</div>
  <div class="abs footer-link" style="left:122px;top:1095px">Parts</div>
  <div class="abs footer-link" style="left:122px;top:1105px">Trucks/Trailers</div>
  <div class="abs footer-link" style="left:122px;top:1115px">Finance</div>
  <div class="abs footer-head" style="left:192px;top:1051px">Contact Us</div>
  <div class="abs footer-row" style="left:192px;top:1068px"><span class="ico"><svg width="6" height="5" viewBox="0 0 10 8"><rect x=".5" y=".5" width="9" height="7" fill="none" stroke="#fff"/><path d="M.5.5L5 4 9.5.5" fill="none" stroke="#fff"/></svg></span>info@torvane.com</div>
  <div class="abs footer-row" style="left:192px;top:1088px"><span class="ico"><svg width="5" height="7" viewBox="0 0 6 8"><path d="M3 8S0 4.5 0 3a3 3 0 016 0c0 1.5-3 5-3 5z" fill="#fff"/><circle cx="3" cy="3" r="1" class="fill-accent"/></svg></span>Lorem ipsum,torvane,USA</div>
  <div class="abs footer-row" style="left:192px;top:1107px"><span class="ico"><svg width="6" height="6" viewBox="0 0 10 10"><path d="M2 1l2 2-1 1.5c.8 1.5 1.8 2.5 3.3 3.3L7.8 6.8l2 2-1.3 1.2C4.6 9.6.4 5.4 0 1.5z" fill="#fff"/></svg></span>+1(555)014 2290</div>
  <div class="abs footer-head" style="left:283px;top:1051px">Follow Us</div>
  <span class="abs social" style="left:283px"></span><span class="abs social" style="left:301px"></span><span class="abs social" style="left:318px"></span>
  <div class="abs copyright">Copyright © 2024 Torvane. | All Rights Reserved</div>

  <div class="abs shade"></div>
  <div class="abs popup">
    <div class="popup-title">VISIT OUR PRE-PURCHASE<br>INSPECTIONS</div>
    <p class="popup-copy">Lorem ipsum dolor sit amet, consectetur adipiscing elit, sed do eiusmod tempor incididunt ut labore et dolore magna aliqua. Quis ipsum suspendisse ultrices gravida. Risus commodo viverra maecenas accumsan lacus vel facilisis.</p>
    <div class="btn" style="left:95px;top:95px;width:40px;height:12px">Click Here</div>
  </div>
</section>

</body>
</html>
```